Business Card Design Project : Tidewell Press

In preparation for market launch, Whistler's Tidewell Press require the development of a business card. Tidewell Press is a Community online publishing web portal. We provide the the city of Whistler located in B.C. (Canada) business directories, News, Classified ads, News, Events and blogs etc.

The main focus of the brand is to help local businesses to corporate with their online advertisement and marketing. Meeting our clients face to face is a must (B2B).

Target Market(s)

The target market is B2B customers. Business Owners to Marketing, advertising Managers

Industry/Entity Type

Business

Requirements
Must have
• - The business card will be two sided.
the BACK side will have our logo which consist of (icon, url,slogan) submited. The logo will be middle and centred.

The FRONT side should have company details:

Company Legal Name: FERNDALE TIDEWELL PRESS

Owen Marsk
Director of Sales & Marketing

www.ferndaletidewell.biz
owen@ferndaletidewell.biz

Phone: 555 014 3826
#2817 - 562 E. Harlow Ave.
Vancouver, B.C. K7P2R4 Canada
Nice to have
• - For the "FRONT" side of our business card. You can separate or re-arrange with our logo components (icon, logo,slogan). It does not have to be together.

Also our company legal name is rather long so arrange or organize the name in a way to make it shorter. Your experience and creativity will have to come in play.
Should not have
• should not have other colors beside logo color and black text (2 colors). Also nothing Three dimensional

```html
<!DOCTYPE html>
<html lang="en">
<head>
<meta charset="utf-8">
<title>Ferndale Tidewell Press – Business Card</title>
<link href="https://fonts.googleapis.com/css2?family=Open+Sans:wght@400;600;700&family=PT+Sans+Narrow:wght@400;700&display=swap" rel="stylesheet">
<style>
  :root {
    --brand-blue: #3b8ff0;
    --ink: #111111;
    --paper: #ffffff;
    --backdrop: #e4e6e8;
    --card-shadow: rgba(0, 0, 0, 0.14);
  }
  * { margin: 0; padding: 0; box-sizing: border-box; }
  html, body {
    width: 1200px; height: 1200px; overflow: hidden;
    background: var(--backdrop);
    font-family: "Open Sans", Arial, sans-serif;
    color: var(--ink);
  }
  .canvas { position: relative; width: 1200px; height: 1200px; }

  .card {
    position: absolute; left: 190px; width: 820px; height: 470px;
    background: var(--paper);
    box-shadow: 0 4px 18px var(--card-shadow);
    overflow: hidden;
  }
  .card--front { top: 95px; }
  .card--back  { top: 635px; }

  /* Front */
  .front-brand {
    position: absolute; left: 200px; top: 62px;
    display: flex; align-items: center; gap: 22px;
  }
  .brand-dot {
    width: 78px; height: 78px; border-radius: 50%;
    background: var(--brand-blue);
  }
  .brand-name {
    font-family: "PT Sans Narrow", "Arial Narrow", sans-serif;
    font-weight: 700; font-size: 44px; line-height: 1;
    letter-spacing: 1px; color: var(--ink);
  }
  .front-address {
    position: absolute; right: 62px; top: 190px;
    text-align: center; font-size: 19px; line-height: 1.3;
  }
  .contact {
    position: absolute; left: 58px; bottom: 48px;
  }
  .contact-name {
    font-size: 34px; font-weight: 400; color: var(--brand-blue);
    letter-spacing: 1px; line-height: 1.15;
  }
  .contact-title { font-size: 18px; margin-top: 4px; }
  .contact-email { font-size: 20px; margin-top: 4px; }

  /* Back */
  .back-brand {
    position: absolute; left: 0; right: 0; top: 118px;
    display: flex; justify-content: center; align-items: center; gap: 16px;
  }
  .back-brand .brand-dot { width: 46px; height: 46px; }
  .back-brand .brand-name { font-size: 36px; color: var(--brand-blue); }
  .back-band {
    position: absolute; left: 0; right: 0; top: 196px; height: 24px;
    background: var(--brand-blue);
  }
  .back-url {
    position: absolute; left: 0; right: 0; top: 228px;
    text-align: center; font-weight: 700; font-size: 26px;
  }
  .back-slogan {
    position: absolute; left: 0; right: 0; top: 266px;
    text-align: center; font-size: 16px; color: var(--brand-blue);
  }
</style>
</head>
<body>
<main class="canvas">

  <section class="card card--front" aria-label="Business card front">
    <div class="front-brand">
      <span class="brand-dot"></span>
      <div class="brand-name">FERNDALE<br>TIDEWELL PRESS</div>
    </div>

    <address class="front-address" style="font-style: normal;">
      #2817 - 562 E. Harlow<br>
      Ave. Vancouver, B.C. K7P2R4<br>
      CANADA<br>
      Phone: 555 014 3826
    </address>

    <div class="contact">
      <div class="contact-name">Owen Marsk</div>
      <div class="contact-title">Director of Sales &amp; Marketing</div>
      <div class="contact-email">owen@ferndaletidewell.biz</div>
    </div>
  </section>

  <section class="card card--back" aria-label="Business card back">
    <div class="back-brand">
      <span class="brand-dot"></span>
      <div class="brand-name">FERNDALE TIDEWELL PRESS</div>
    </div>
    <div class="back-band"></div>
    <div class="back-url">www.ferndaletidewell.biz</div>
    <div class="back-slogan">Your information gateway</div>
  </section>

</main>
</body>
</html>
```